Webiste Design KLV

Design the website using uploaded content. Design colors should match that of the company logo with an allowance of one more extra color if it makes the website look much better and colorful. Use Technology related stock images in your design.

Target Market(s)

Potential Clients - Companies

Industry/Entity Type

Information Technology

Coding

Coded - Design and coding required

Number of Pages Required

5+ page

Requirements
Must have
• Company Logo Colors
Nice to have
• Professional Look and Feel with Sliders showing professional information technology images

```html
<!DOCTYPE html>
<html lang="en">
<head>
<meta charset="utf-8">
<title>KLV Technologies</title>
<link href="https://fonts.googleapis.com/css2?family=Poppins:wght@300;400;500;600&display=swap" rel="stylesheet">
<style>
:root{
  --orange:#f7861e;
  --orange-soft:#fde3c8;
  --brown:#5b3411;
  --brown-card:#b8611e;
  --ink:#1f1f1f;
  --muted:#6d6d6d;
  --field:#f4f4f4;
  --sky:#eaf2fb;
  --stage:#85868a;
}
*{margin:0;padding:0;box-sizing:border-box}
html,body{width:1200px;height:3438px;overflow:hidden}
body{background:var(--stage);font-family:'Poppins',sans-serif;color:var(--ink);position:relative}
.page{position:absolute;left:140px;top:143px;width:921px;height:3152px;background:#fff;overflow:hidden}
.abs{position:absolute}
.topbar{left:0;top:0;width:921px;height:24px;border-bottom:1px solid #eee;font-size:7px;color:#555}
.topbar span{position:absolute;top:8px;display:flex;align-items:center;gap:4px}
.dot{display:inline-block;width:8px;height:8px;border-radius:50%;background:var(--orange)}
.social{position:absolute;top:6px;display:flex;gap:7px}
.social i{width:11px;height:11px;border-radius:50%;background:var(--orange);display:block}
.nav{left:0;top:24px;width:921px;height:47px;border-bottom:1px solid #eee}
.brand{position:absolute;left:180px;top:13px;font-size:20px;font-weight:600;color:var(--orange);display:flex;align-items:center;gap:6px}
.brand b{width:14px;height:14px;background:var(--ink);display:block}
.menu{position:absolute;left:348px;top:18px;display:flex;gap:16px;font-size:10px}
.btn{background:var(--orange);color:#fff;border-radius:14px;font-size:8px;display:flex;align-items:center;justify-content:center}
.hero{left:0;top:71px;width:921px;height:360px;background:var(--orange)}
.hero-dark{left:702px;top:71px;width:219px;height:360px;background:linear-gradient(160deg,#0b2a5a,#123c7a 60%,#0a1d45)}
.hero-art{left:531px;top:105px;width:292px;height:292px;border-radius:50%;border:6px solid #fff;background:radial-gradient(circle at 50% 45%,#7a8fe0,#3a34a8 55%,#1a1f6b)}
.eyebrow{color:var(--orange);font-size:9px;font-weight:500}
.title{font-size:17px;font-weight:500}
.step{width:160px;height:160px;border-radius:50%;border:3px solid var(--orange-soft);display:flex;flex-direction:column;align-items:center;justify-content:center;text-align:center;padding:0 24px}
.step h4{font-size:10px;font-weight:500;margin-bottom:6px}
.step p{font-size:6.5px;color:var(--muted);line-height:1.4}
.badge{width:24px;height:24px;border-radius:50%;background:var(--orange);color:#fff;font-size:9px;display:flex;align-items:center;justify-content:center;border:2px solid #fff}
.photo{border-radius:2px}
.bar-label{font-size:7px;display:flex;justify-content:space-between;width:270px}
.bar{width:270px;height:4px;background:var(--orange-soft);border-radius:2px}
.bar i{display:block;height:4px;width:175px;background:var(--orange);border-radius:2px}
.band{left:0;top:1403px;width:921px;height:473px;background:var(--brown)}
.card{width:180px;height:216px;background:var(--brown-card);color:#fff;text-align:center}
.card .pic{position:absolute;left:20px;top:18px;width:140px;height:88px}
.card h4{position:absolute;top:138px;width:100%;font-size:10px;font-weight:500}
.card p{position:absolute;top:160px;left:16px;right:16px;font-size:6.5px;line-height:1.4}
.stat{text-align:center;width:120px}
.stat b{display:block;color:var(--orange);font-size:22px;font-weight:500}
.stat span{font-size:6.5px;color:#555}
.testimonials{left:0;top:1977px;width:921px;height:361px;background:var(--sky)}
.round{border-radius:50%;border:5px solid #fff}
.plate{width:70px;height:26px;border-radius:4px;background:#d9dde3}
.field{background:var(--field);font-size:7px;color:#777;padding:9px 12px}
.footer{left:0;top:2925px;width:921px;height:227px;background:var(--orange);color:#fff}
.footer h5{position:absolute;top:33px;font-size:12px;font-weight:600}
.footer .txt{position:absolute;font-size:6.5px;line-height:1.55}
</style>
</head>
<body>
<div class="page">
  <div class="abs topbar">
    <span style="left:180px"><i class="dot"></i>010 555 0142</span>
    <span style="left:288px"><i class="dot"></i>hello@klvtech.example</span>
    <span style="left:406px"><i class="dot"></i>Harbor Lane North Bay</span>
    <div class="social" style="left:676px"><i></i><i></i><i></i></div>
  </div>
  <div class="abs nav">
    <div class="brand"><b></b>KLV</div>
    <div class="menu"><span>Home</span><span>About</span><span>Services</span><span>Hosting</span><span>Contact Us</span></div>
    <div class="abs btn" style="left:660px;top:11px;width:82px;height:27px">Start A Project</div>
  </div>

  <div class="abs hero"></div>
  <div class="abs hero-dark" role="img" aria-label="Blue circuit technology background"></div>
  <div class="abs" style="left:180px;top:144px;color:#fff">
    <div style="font-size:13px;font-weight:500">KLV Technologies</div>
    <div style="font-size:29px;font-weight:500;line-height:1.2;margin-top:14px">Awesome IT Services<br>For Your Business</div>
    <p style="font-size:8.5px;line-height:1.35;width:312px;margin-top:18px;opacity:.9">Our vision is to be the most innovative and preferred ICT and Engineering Company. We therefore intend to grow the business locally and internationally.</p>
    <div class="btn" style="background:#fff;color:var(--orange);width:71px;height:24px;margin-top:30px">Learn More</div>
  </div>
  <div class="abs hero-art" role="img" aria-label="Artificial intelligence technology illustration"></div>

  <div class="abs eyebrow" style="left:0;width:921px;text-align:center;top:484px">How We Work</div>
  <div class="abs title" style="left:0;width:921px;text-align:center;top:505px">Our Work Process</div>
  <div class="abs step" style="left:177px;top:551px"><h4>Create a Plan</h4><p>Lorem ipsum dolor sit amet, consectetur adipiscing elit, sed do eiusmod tempor incididunt</p></div>
  <div class="abs step" style="left:377px;top:551px"><h4>Start Working</h4><p>Lorem ipsum dolor sit amet, consectetur adipiscing elit, sed do eiusmod tempor incididunt</p></div>
  <div class="abs step" style="left:581px;top:551px"><h4>Publish business</h4><p>Lorem ipsum dolor sit amet, consectetur adipiscing elit, sed do eiusmod tempor incididunt</p></div>
  <div class="abs badge" style="left:299px;top:562px">01</div>
  <div class="abs badge" style="left:499px;top:562px">02</div>
  <div class="abs badge" style="left:703px;top:562px">03</div>
  <svg class="abs" style="left:337px;top:624px" width="40" height="14"><path d="M2 7h34M30 2l6 5-6 5" stroke="#f7b97a" stroke-width="1.5" fill="none"/></svg>
  <svg class="abs" style="left:537px;top:624px" width="40" height="14"><path d="M2 7h34M30 2l6 5-6 5" stroke="#f7b97a" stroke-width="1.5" fill="none"/></svg>

  <div class="abs" style="left:180px;top:781px;display:flex;gap:14px;font-size:8px;color:var(--orange)">
    <span style="background:var(--orange);color:#fff;padding:4px 14px">Mission</span><span style="padding:4px 0">Vission</span><span style="padding:4px 0">Who We Are</span>
  </div>
  <div class="abs" style="left:180px;top:817px;font-size:17px;font-weight:500">MISSION STATEMENT</div>
  <p class="abs" style="left:180px;top:848px;width:264px;font-size:7px;line-height:1.7;color:var(--muted);text-align:justify">To provide and run ICT as well as Engineering solutions and services that allows our customers to focus on achieving their business objectives. We will take care of your technology issues so that you can focus on running and growing your business. Our goal is to increase the productivity, efficiency, and net profits of your company by replacing or collaborating with your existing IT staff to provide a secure, reliable, and stable technology environment.</p>
  <div class="abs" style="left:180px;top:949px;display:flex;gap:26px;font-size:10px;align-items:center">
    <span style="display:flex;align-items:center;gap:8px"><i style="width:26px;height:26px;border-radius:50%;border:2px solid var(--orange-soft);display:block"></i>Lorem ipsum</span>
    <span style="display:flex;align-items:center;gap:8px"><i style="width:26px;height:26px;border-radius:50%;border:2px solid var(--orange-soft);display:block"></i>Lorem Ipsum</span>
  </div>
  <div class="abs btn" style="left:180px;top:996px;width:71px;height:26px">Learn More</div>
  <div class="abs" style="left:558px;top:748px;width:46px;height:46px;border-radius:50%;background:var(--orange)"></div>
  <div class="abs" style="left:640px;top:778px;width:145px;height:205px;border-radius:90px 0 0 0;background:var(--orange)"></div>
  <div class="abs" style="left:758px;top:982px;width:22px;height:22px;border-radius:50%;background:var(--orange)"></div>
  <div class="abs photo" style="left:514px;top:772px;width:132px;height:155px;background:linear-gradient(#d9e0e6,#9aa8b4)" role="img" aria-label="Business meeting photo"></div>
  <div class="abs photo" style="left:658px;top:806px;width:132px;height:181px;background:linear-gradient(#4a4d57,#a57867)" role="img" aria-label="Developer working at computer"></div>
  <div class="abs photo" style="left:514px;top:941px;width:132px;height:82px;background:linear-gradient(#3a3f48,#776458)" role="img" aria-label="People working at computers"></div>

  <div class="abs" style="left:169px;top:1070px;width:46px;height:46px;border-radius:50%;background:var(--orange)"></div>
  <div class="abs" style="left:250px;top:1099px;width:235px;height:246px;border-radius:120px 120px 120px 0;background:var(--orange)"></div>
  <div class="abs" style="left:375px;top:1340px;width:20px;height:20px;border-radius:50%;background:var(--orange)"></div>
  <div class="abs photo" style="left:127px;top:1092px;width:132px;height:155px;background:linear-gradient(#0e2348,#2e5e97)" role="img" aria-label="Cloud upload network graphic"></div>
  <div class="abs photo" style="left:274px;top:1128px;width:132px;height:181px;background:radial-gradient(circle,#4f9fe6,#0c2a63)" role="img" aria-label="Cloud security graphic"></div>
  <div class="abs photo" style="left:127px;top:1262px;width:132px;height:82px;background:linear-gradient(#7d6a5c,#c7b5a4)" role="img" aria-label="Team hands together photo"></div>
  <div class="abs eyebrow" style="left:471px;top:1141px;font-size:8px">Our Experties</div>
  <div class="abs" style="left:471px;top:1158px;font-size:17.5px;line-height:1.3">We Are Increasing Business<br>Success With Technology</div>
  <div class="abs" style="left:471px;top:1221px"><div class="bar-label"><span>Cloud Services</span><span>65%</span></div><div class="bar" style="margin-top:6px"><i></i></div></div>
  <div class="abs" style="left:471px;top:1253px"><div class="bar-label"><span>Security Services</span><span>65%</span></div><div class="bar" style="margin-top:6px"><i></i></div></div>
  <div class="abs" style="left:471px;top:1285px"><div class="bar-label"><span>Storage solutions,</span><span>65%</span></div><div class="bar" style="margin-top:6px"><i></i></div></div>

  <div class="abs band" role="img" aria-label="Network mesh pattern over dark brown"></div>
  <div class="abs" style="left:0;width:921px;text-align:center;top:1458px;color:#fff;font-size:8px">Technology Solution</div>
  <div class="abs" style="left:0;width:921px;text-align:center;top:1477px;color:#fff;font-size:17.5px">We Provide IT &amp; business Solution</div>
  <div class="abs card" style="left:180px;top:1526px"><div class="pic" style="background:linear-gradient(#0d8a8a,#0c4e6b)" role="img" aria-label="Server management illustration"></div><h4>Server Management</h4><p>Lorem ipsum dolor sit amet, consectetur adipiscing elit, sed do eiusmod tempor incididunt ut labore et dolore magna aliqua. Quis</p></div>
  <div class="abs card" style="left:369px;top:1526px"><div class="pic" style="background:linear-gradient(#2f7fd6,#c7def5)" role="img" aria-label="Network management illustration"></div><h4>Network Management</h4><p>Lorem ipsum dolor sit amet, consectetur adipiscing elit, sed do eiusmod tempor incididunt ut labore et dolore magna aliqua. Quis</p></div>
  <div class="abs card" style="left:561px;top:1526px"><div class="pic" style="background:linear-gradient(#f36f73,#f59a8f)" role="img" aria-label="Email management illustration"></div><h4>Email Management</h4><p>Lorem ipsum dolor sit amet, consectetur adipiscing elit, sed do eiusmod tempor incididunt ut labore et dolore magna aliqua. Quis</p></div>
  <div class="abs" style="left:432px;top:1766px;display:flex;gap:3px"><i style="width:10px;height:2px;background:#fff"></i><i style="width:10px;height:2px;background:#fff"></i><i style="width:10px;height:2px;background:#fff"></i><i style="width:10px;height:2px;background:#fff"></i></div>

  <div class="abs stat" style="left:186px;top:1905px"><b>3000+</b><span>Project Done</span></div>
  <div class="abs stat" style="left:348px;top:1905px"><b>8000+</b><span>Active Clients</span></div>
  <div class="abs stat" style="left:495px;top:1905px"><b>20+</b><span>Glorious Year</span></div>
  <div class="abs stat" style="left:634px;top:1905px"><b>900+</b><span>Project Win</span></div>

  <div class="abs testimonials" role="img" aria-label="Dotted world map background"></div>
  <div class="abs eyebrow" style="left:180px;top:2066px;font-size:8px">Testimonial</div>
  <div class="abs" style="left:180px;top:2080px;font-size:17.5px">What Our Clients Say</div>
  <div class="abs" style="left:180px;top:2112px;font-size:34px;color:var(--orange);line-height:1">“</div>
  <p class="abs" style="left:180px;top:2126px;width:256px;font-size:7px;line-height:2">&nbsp;&nbsp;&nbsp;&nbsp;&nbsp;&nbsp;&nbsp;&nbsp;&nbsp;Lorem ipsum dolor sit amet, consectetur adipiscing elit, sed do eiusmod tempor incididunt ut labore et dolore magna aliqua. Quis ipsum suspendisse ultrices gravida. Risus commodo viverra maecenas accumsan lacus vel facilisis enas.</p>
  <div class="abs" style="left:400px;top:2170px;font-size:34px;color:var(--orange);line-height:1">”</div>
  <div class="abs" style="left:178px;top:2195px;width:48px;height:48px;border-radius:50%;border:2px solid var(--orange);background:#e7d3c3" role="img" aria-label="Client portrait"></div>
  <div class="abs" style="left:234px;top:2211px;font-size:8px;line-height:1.3"><span style="color:var(--orange);font-weight:500">Lorem Ipsum</span><br>Artist</div>
  <div class="abs" style="left:180px;top:2264px;display:flex;gap:3px"><i style="width:10px;height:2px;background:var(--orange)"></i><i style="width:10px;height:2px;background:var(--orange)"></i><i style="width:10px;height:2px;background:var(--orange)"></i><i style="width:10px;height:2px;background:var(--orange)"></i></div>
  <div class="abs round" style="left:474px;top:2040px;width:146px;height:146px;background:linear-gradient(#9fb2c5,#dfe7ee)" role="img" aria-label="Client using laptop photo"></div>
  <div class="abs round" style="left:637px;top:2037px;width:94px;height:94px;background:linear-gradient(#c9cfc2,#7a8b84)" role="img" aria-label="Client working photo"></div>
  <div class="abs round" style="left:609px;top:2144px;width:112px;height:112px;background:linear-gradient(#d6dbe0,#9aa2aa)" role="img" aria-label="Client on phone photo"></div>
  <div class="abs round" style="left:521px;top:2198px;width:66px;height:66px;background:radial-gradient(circle,#f6d33c,#c98a5a)" role="img" aria-label="Smiley feedback photo"></div>

  <div class="abs eyebrow" style="left:180px;top:2399px;font-size:7px;letter-spacing:1px">PARTNERSHIP</div>
  <div class="abs" style="left:180px;top:2417px;font-size:27px;line-height:1.25">Check Out Best<br>Clients &amp; Parthners</div>
  <p class="abs" style="left:507px;top:2421px;width:230px;font-size:7.5px;line-height:1.4">When an unknown printer took a galley of type and scrambled it to make a type specimen book.</p>
  <p class="abs" style="left:507px;top:2453px;width:230px;font-size:7.5px;line-height:1.4">When an unknown printer took a galley of type and scrambled it to make a type specimen book.</p>
  <div class="abs plate" style="left:177px;top:2519px"></div>
  <div class="abs plate" style="left:273px;top:2519px"></div>
  <div class="abs plate" style="left:372px;top:2519px"></div>
  <div class="abs plate" style="left:479px;top:2519px"></div>
  <div class="abs plate" style="left:582px;top:2519px"></div>
  <div class="abs plate" style="left:671px;top:2519px"></div>

  <div class="abs eyebrow" style="left:0;width:921px;text-align:center;top:2601px;font-size:8px">Contact Us</div>
  <div class="abs" style="left:0;width:921px;text-align:center;top:2618px;font-size:17.5px">We Are Provide Best Service</div>
  <div class="abs field" style="left:180px;top:2677px;width:270px;height:28px">Name</div>
  <div class="abs field" style="left:468px;top:2677px;width:273px;height:28px">Email</div>
  <div class="abs field" style="left:180px;top:2718px;width:270px;height:28px">Phone Number</div>
  <div class="abs field" style="left:468px;top:2718px;width:273px;height:28px">Select Service<svg style="position:absolute;right:12px;top:11px" width="8" height="6"><path d="M1 1l3 3 3-3" stroke="#555" fill="none"/></svg></div>
  <div class="abs field" style="left:180px;top:2754px;width:561px;height:68px">Message</div>
  <div class="abs" style="left:180px;top:2844px;width:90px;height:32px;background:var(--orange);color:#fff;font-size:7.5px;display:flex;align-items:center;justify-content:center">CONTACT US</div>

  <div class="abs footer">
    <h5 style="left:109px">ABOUT US</h5>
    <p class="txt" style="left:109px;top:54px;width:220px">Lorem ipsum dolor sit amet, consectetur adipiscing elit. Nullam non ornare risus, luctus molestie lorem. Aenean sit amet ipsum quis mauris pellentesque rutrum. Nam id ipsum vitae mauris lobortis mattis semper placerat tellus. Duis molestie odio a vestibulum dignissim. Sed sollicitudin arcu sollicitudin, fermentum ligula vitae, convallis ante.</p>
    <div class="abs" style="left:109px;top:147px;display:flex;gap:6px"><i style="width:14px;height:14px;border-radius:50%;background:#fff;display:block"></i><i style="width:14px;height:14px;border-radius:50%;background:#fff;display:block"></i><i style="width:14px;height:14px;border-radius:50%;background:#fff;display:block"></i><i style="width:14px;height:14px;border-radius:50%;background:#fff;display:block"></i></div>
    <h5 style="left:406px">NAVIGATION</h5>
    <p class="txt" style="left:406px;top:54px;line-height:2.3">HOME<br>ABOUT US<br>FEATURES<br>SERVICES<br>CONTACT US</p>
    <h5 style="left:606px">ADDRESS</h5>
    <p class="txt" style="left:606px;top:54px">NORTH REGION<br>12 Elm Street, Riverside 0600<br>P. O. Box 10000, Riverside 0700<br><br>CENTRAL REGION<br>Building 2, 8 Oak Avenue, Hillview 2000<br>Po Box 500, Hillview 2001</p>
    <p class="txt" style="left:606px;top:132px;font-size:8.5px;line-height:1.45">Email: info@klvtech.example<br>Phone: 010 555 0142<br>Fax: 010 555 0199<br>Co Reg No: 2020/000000/07</p>
    <div class="abs" style="left:858px;top:124px;background:#fff;color:var(--orange);font-size:6.5px;padding:2px 8px;border-radius:3px">Live Chat</div>
    <div class="abs" style="left:870px;top:143px;width:38px;height:38px;border-radius:50%;background:#fff"></div>
    <div class="abs" style="left:0;top:205px;width:921px;border-top:1px solid rgba(255,255,255,.5);text-align:center;font-size:6.5px;padding-top:6px">© 2023 KLV . All Rights Reserved. Developed by KLV.</div>
  </div>
</div>
</body>
</html>
```